Geschäftspapiere für ein Bauunternehmen
Zielgruppe
Meine Firma ist ein Bauunternehmen und suchen ein Modernes aber auch hochwertiges Design für unsere Geschäftspapiere und unsere Zielgruppen sind Private Kunden die ein oder mehrere Häuser bauen wollen.
Aufgabenstellung
Das Design soll sehr modern aber auch hochwertig sein.

```html
<!DOCTYPE html>
<html lang="de">
<head>
<meta charset="utf-8">
<title>Korvanbau – Briefbogen</title>
<link rel="stylesheet" href="https://fonts.googleapis.com/css2?family=Montserrat:wght@700&display=swap">
<style>
  :root {
    --paper: #ffffff;
    --ink: #1a1a1a;
    --brand-red: #c0282d;
    --faint-grey: #dcdcdc;
  }
  html, body {
    margin: 0;
    padding: 0;
    overflow: hidden;
    background: var(--paper);
  }
  .letterhead {
    position: relative;
    width: 848px;
    height: 1200px;
    background: var(--paper);
    overflow: hidden;
    font-family: "Montserrat", Arial, sans-serif;
  }
  .brand {
    position: absolute;
    top: 150px;
    right: 56px;
    display: flex;
    align-items: center;
    gap: 10px;
  }
  .brand-square {
    width: 22px;
    height: 22px;
    background: var(--brand-red);
  }
  .brand-name {
    font-weight: 700;
    font-size: 19px;
    letter-spacing: 1.5px;
    color: var(--ink);
  }
  .brand-watermark {
    position: absolute;
    left: -12px;
    bottom: 40px;
    margin: 0;
    font-weight: 700;
    font-size: 150px;
    line-height: 1;
    letter-spacing: -2px;
    color: var(--faint-grey);
    writing-mode: vertical-rl;
    transform: rotate(180deg);
    white-space: nowrap;
  }
</style>
</head>
<body>
  <main class="letterhead">
    <header class="brand">
      <span class="brand-square" aria-hidden="true"></span>
      <span class="brand-name">KORVANBAU</span>
    </header>
    <p class="brand-watermark" aria-hidden="true">KORVAN</p>
  </main>
</body>
</html>
```